Oil and Gas Industry training School Needs a Web Design

We need a web design for a new company based in Northern British Columbia Canada called "SKILLSPAN Industry Training Inc." Is a training facility that specializes in different aspects of Pipeline Construction training. We also offer compliance courses for Oil and Gas Industry. We would like to see designs that us the colours in our logo.

Target Market(s)

Is Men and women between 18-60 that want to work in the oil and gas industry

Industry/Entity Type

School

Number of Pages Required

5+ page

Font styles to use
Sans Serif

Colors
f37022
000000
333333
ffffff
848484
7f7f7f
c8c8c8
f68d4d
fee3d4

Requirements
Must have
• a easy back end for editing content! and adding additional pages if necessary.

```html
<!DOCTYPE html>
<html lang="en">
<head>
<meta charset="utf-8">
<title>SKILLSPAN Industry Training Inc.</title>
<link rel="stylesheet" href="https://fonts.googleapis.com/css2?family=Open+Sans:wght@400;600;700&family=Noto+Serif:wght@400&display=swap">
<style>
:root{
  --orange:#f37022;
  --orange-light:#f68d4d;
  --orange-pale:#fee3d4;
  --black:#000000;
  --ink:#333333;
  --white:#ffffff;
  --grey:#848484;
  --grey-2:#7f7f7f;
  --line:#c8c8c8;
  --rule:#e6e6e6;
  --footer:#2b2b2b;
  --footer-bar:#222222;
}
*{margin:0;padding:0;box-sizing:border-box}
html,body{width:1200px;height:2980px;overflow:hidden;background:var(--white)}
body{font-family:"Open Sans",Arial,sans-serif;color:var(--ink);position:relative}
.abs{position:absolute}
p{font-size:12.5px;line-height:20px;color:var(--grey)}
a{color:inherit;text-decoration:none}

/* header */
.site-header{position:absolute;left:0;top:0;width:1200px;height:84px;background:var(--white)}
.brand{position:absolute;left:130px;top:16px;display:flex;align-items:center;gap:10px}
.brand-dot{width:44px;height:44px;border-radius:50%;background:var(--ink)}
.brand-name{font-size:26px;font-weight:700;color:var(--ink);letter-spacing:.5px;line-height:28px}
.brand-sub{font-size:10px;color:var(--grey);letter-spacing:1.5px;border-top:1px solid var(--line);margin-top:2px;padding-top:2px;text-align:center}
.main-nav{position:absolute;right:122px;top:34px;display:flex;gap:26px;font-size:12.5px;font-weight:600;color:var(--ink)}
.main-nav .active{color:var(--orange);position:relative}
.main-nav .active::after{content:"";position:absolute;left:-8px;right:-8px;top:48px;height:4px;background:var(--orange)}

/* hero */
.hero{position:absolute;left:0;top:84px;width:1200px;height:428px;background:linear-gradient(90deg,#1c2024 0%,#3a3f44 45%,#4b5056 70%,#2a2e32 100%)}
.hero-worker{position:absolute;left:740px;top:0;width:320px;height:428px;background:linear-gradient(180deg,#6d7a80 0%,#3d6f7c 55%,#2f5966 100%);opacity:.9}
.hero-tag{position:absolute;left:130px;background:var(--white);border-left:8px solid var(--orange);color:var(--orange);font-weight:700;font-size:22px;letter-spacing:.5px;padding:0 20px;height:50px;line-height:50px}
.hero-btn{position:absolute;left:130px;top:324px;background:var(--white);color:var(--orange);font-size:13px;font-weight:600;padding:0 18px;height:40px;line-height:40px;border-radius:2px}

/* services */
.service{position:absolute;top:566px;width:280px}
.service-img{width:280px;height:184px}
.service h3{font-size:15px;font-weight:700;color:var(--ink);margin:12px 0 6px}
.rule{position:absolute;left:0;width:1200px;height:1px;background:var(--rule)}

/* about */
.section-title{font-size:26px;font-weight:600;letter-spacing:1.5px;color:var(--ink)}
.section-title .hl{color:var(--orange)}
.title-line{position:absolute;height:1px;background:var(--line)}
.title-line::after{content:"";position:absolute;right:-5px;top:-4px;width:9px;height:9px;border-radius:50%;border:1px solid var(--line);background:var(--white)}
.about-copy{position:absolute;left:130px;top:1030px;width:444px;text-align:right}
.about-copy p+p{margin-top:10px}
.about-copy b{color:var(--orange);font-weight:600}
.btn-outline{position:absolute;border:1px solid var(--line);height:42px;line-height:40px;text-align:center;font-size:13px;color:var(--ink);background:var(--white)}
.timeline-line{position:absolute;left:659px;top:960px;width:0;height:360px;border-left:2px dotted var(--orange)}
.tl-icon{position:absolute;left:630px;width:60px;height:60px;border-radius:50%;background:var(--orange);display:flex;align-items:center;justify-content:center}
.tl-item{position:absolute;left:718px;width:362px}
.tl-item h4{font-size:15px;font-weight:600;color:var(--ink);margin-bottom:6px}
.tl-item b{color:var(--orange);font-weight:600}

/* testimonials */
.quote{position:absolute;width:360px}
.avatar{position:absolute;width:74px;height:74px;border-radius:50%;background:radial-gradient(circle at 50% 35%,#f5c83a 0 30%,#e9c9a5 31% 60%,#d9d9d9 61%);border:3px solid var(--white);box-shadow:0 0 0 1px var(--rule)}
.quote .who{font-size:13px;font-weight:600;color:var(--ink);margin-top:14px}
.quote .role{font-size:12.5px;color:var(--grey);margin-top:4px}
.quote .role span{color:var(--orange)}

/* cta */
.cta-band{position:absolute;left:0;top:2460px;width:1200px;height:176px;background:linear-gradient(90deg,#2c2823,#4a3e33 50%,#2c2823)}
.cta-box{position:absolute;left:130px;top:26px;width:956px;height:124px;background:var(--white)}
.cta-box p{position:absolute;left:40px;top:40px;width:650px;text-align:center;font-size:12.5px}
.cta-btn{position:absolute;right:36px;top:40px;width:112px;height:42px;border:1px solid var(--line);color:var(--orange);font-weight:600;font-size:14px;text-align:center;line-height:40px}

/* footer */
.site-footer{position:absolute;left:0;top:2636px;width:1200px;height:314px;background:var(--footer)}
.f-col{position:absolute;top:36px}
.f-col h5{font-size:13px;font-weight:600;color:#cfcfcf;letter-spacing:1px;margin-bottom:14px}
.f-col p{color:#e6e6e6;font-size:12.5px}
.news{display:flex;gap:14px;margin-bottom:14px}
.news i{width:30px;height:30px;background:#e6e6e6;flex:none}
.news span{font-size:11px;color:#fff;line-height:16px}
.news small{display:block;color:#9a9a9a;font-size:10px}
.tags{display:flex;gap:6px}
.tags span{background:#f2f2f2;color:#333;font-size:11px;padding:2px 8px}
.cats{font-family:"Noto Serif",Georgia,serif;font-size:12.5px;color:#fff;line-height:20px}
.social{display:flex;gap:32px;margin-top:36px}
.social div{display:flex;gap:8px;align-items:center;font-size:10px;color:#fff;line-height:13px}
.social i{width:28px;height:28px;display:block}
.bottom-bar{position:absolute;left:0;top:2950px;width:1200px;height:30px;background:var(--footer-bar);font-size:11px;color:#9a9a9a}
.bottom-bar .copy{position:absolute;left:144px;top:7px;color:#fff}
.bottom-bar .copy span{color:var(--orange)}
.bottom-nav{position:absolute;right:120px;top:7px;display:flex;gap:10px}
.bottom-nav .on{color:var(--orange)}
</style>
</head>
<body>

<header class="site-header">
  <div class="brand">
    <div class="brand-dot"></div>
    <div>
      <div class="brand-name">SKILLSPAN</div>
      <div class="brand-sub">INDUSTRY TRAINING INC.</div>
    </div>
  </div>
  <nav class="main-nav">
    <a class="active">HOME</a><a>COURSE</a><a>FACULTY</a><a>FEES AND FUNDING</a><a>TESTIMONIALS</a><a>FAQ</a><a>CONTACT US</a>
    <svg width="14" height="14" viewBox="0 0 14 14"><circle cx="6" cy="6" r="4.5" fill="none" stroke="#333" stroke-width="2"/><line x1="9.5" y1="9.5" x2="13" y2="13" stroke="#333" stroke-width="2"/></svg>
  </nav>
</header>

<section class="hero" role="img" aria-label="Pipeline plant with smiling worker in hard hat and denim shirt">
  <div class="hero-worker"></div>
  <div class="hero-tag" style="top:120px">PIPELINE DESIGN AND CONSTRUCTION</div>
  <div class="hero-tag" style="top:192px">JOB TRAINING PROGRAMS</div>
  <a class="hero-btn">APPLY NOW</a>
</section>

<section class="services">
  <div class="service" style="left:130px">
    <div class="service-img" role="img" aria-label="Engineers in hard hats at an oil pump site" style="background:linear-gradient(180deg,#6fa6d8,#c9b08a 60%,#d9742e)"></div>
    <h3>Consulting</h3>
    <p>Lorem ipsum dolor sit amet, consectetuer adipiscing elit.</p>
  </div>
  <div class="service" style="left:466px">
    <div class="service-img" role="img" aria-label="Trainees in high visibility vests in a workshop" style="background:linear-gradient(180deg,#4c5560,#3a5a8a 55%,#c9c84a)"></div>
    <h3>Training</h3>
    <p>Lorem ipsum dolor sit amet, consectetuer adipiscing elit.</p>
  </div>
  <div class="service" style="left:802px">
    <div class="service-img" role="img" aria-label="Work boots, gloves and yellow hard hat" style="background:linear-gradient(135deg,#6b3d12,#c9832e 50%,#f0c030)"></div>
    <h3>Products</h3>
    <p>Lorem ipsum dolor sit amet, consectetuer adipiscing elit.</p>
  </div>
</section>

<div class="rule" style="top:866px"></div>

<section class="about">
  <h2 class="section-title abs" style="right:626px;top:924px">ABOUT US</h2>
  <div class="title-line" style="left:426px;top:992px;width:140px"></div>
  <div class="about-copy">
    <p>Lorem ipsum dolor sit amet, consectetuer <b>adipiscing elit.</b> Aenean commodo ligula eget dolor. Aenean massa.</p>
    <p>Nulla consequat massa quis enim.<br>Donec pede justo, fringilla vel, aliquet nec, vulputate eget, arcu.<br>In enim justo, rhoncus ut, imperdiet a, venenatis vitae, justo. Nullam dictum felis eu pede mollis pretium.<br>Integer tincidunt. Cras dapibus. Vivamus elementum semper nisi. Aenean <b>vulputate</b> eleifend tellus.</p>
  </div>
  <div class="title-line" style="left:426px;top:1238px;width:140px"></div>
  <a class="btn-outline" style="left:374px;top:1278px;width:198px">Check out our Team</a>

  <div class="timeline-line"></div>
  <div class="tl-icon" style="top:928px"><svg width="26" height="26" viewBox="0 0 26 26" stroke="#fff" stroke-width="3" stroke-linecap="round"><line x1="5" y1="5" x2="21" y2="21"/><line x1="21" y1="5" x2="5" y2="21"/></svg></div>
  <div class="tl-icon" style="top:1056px"><svg width="24" height="26" viewBox="0 0 24 26" fill="#fff"><rect x="10" y="3" width="3" height="16"/><path d="M13 3h7v5h-7z"/><circle cx="8" cy="19" r="5"/></svg></div>
  <div class="tl-icon" style="top:1160px"><svg width="20" height="28" viewBox="0 0 20 28" fill="#fff"><path d="M12 0L2 16h7l-3 12L18 10h-7z"/></svg></div>
  <div class="tl-icon" style="top:1286px"><svg width="24" height="26" viewBox="0 0 24 26" fill="#fff"><rect x="3" y="2" width="3" height="23"/><path d="M6 3h15l-4 5 4 5H6z"/></svg></div>

  <div class="tl-item" style="top:930px"><h4>Who We Are</h4><p>Aenean vulputate eleifend tellus. Aenean leo ligula, porttitor eu, consequat vitae, eleifend ac, enim. Aliquam lorem ante, dapibus in.</p></div>
  <div class="tl-item" style="top:1056px"><h4>Management Team</h4><p>Donec vitae sapien ut libero venenatis faucibus. Nullam quis ante. Etiam sit amet orci eget eros faucibus tincidunt.</p></div>
  <div class="tl-item" style="top:1160px"><h4>Why Us?</h4><p>Donec sodales sagittis magna. Sed consequat, leo eget bibendum sodales, augue velit cursus nunc, quis gravida magna mi a libero.</p></div>
  <div class="tl-item" style="top:1286px"><h4>Learn More</h4><p>Nullam quis ante. Etiam sit <b>amet orci eget</b> eros faucibus tincidunt. Donec vitae sapien ut libero venenatis faucibus.</p></div>
</section>

<div class="rule" style="top:1412px"></div>

<section class="why">
  <div class="abs" role="img" aria-label="Three pipeline workers in hard hats and coveralls" style="left:130px;top:1510px;width:456px;height:304px;background:linear-gradient(180deg,#dfe9f2 0%,#cdb892 40%,#1f3560 62%,#27406e 100%);border:1px solid var(--rule)"></div>
  <h2 class="section-title abs" style="left:630px;top:1474px">WHY <span class="hl">SKILLSPAN</span></h2>
  <div class="title-line" style="left:636px;top:1544px;width:0"></div>
  <div class="title-line" style="left:640px;top:1544px;width:116px;transform:scaleX(-1)"></div>
  <div class="abs" style="left:630px;top:1580px;width:440px">
    <p>Lorem ipsum dolor sit amet, consectetuer adipiscing elit. Aenean commodo ligula eget dolor. Aenean massa.</p>
    <p style="margin-top:14px">Nulla consequat massa quis enim.Donec pede justo, fringilla vel, aliquet nec, vulputate eget, arcu.In enim justo, rhoncus ut, imperdiet a, venenatis vitae, justo. Nullam dictum felis eu pede mollis pretium.Integer tincidunt. Cras dapibus. Vivamus elementum semper nisi.Aenean vulputate eleifend tellus.</p>
  </div>
  <div class="title-line" style="left:640px;top:1756px;width:116px;transform:scaleX(-1)"></div>
  <a class="btn-outline" style="left:630px;top:1794px;width:112px">Features</a>
</section>

<div class="rule" style="top:1916px"></div>

<section class="testimonials">
  <h2 class="section-title abs" style="left:0;width:1200px;text-align:center;top:1968px">WHAT OTHERS SAY ABOUT US</h2>
  <div class="title-line" style="left:456px;top:2040px;width:140px"></div>
  <div class="title-line" style="left:604px;top:2040px;width:140px;transform:scaleX(-1)"></div>
  <div class="abs" style="left:602px;top:2086px;width:1px;height:300px;background:var(--rule)"></div>
  <div class="abs" style="left:146px;top:2256px;width:438px;height:1px;background:var(--rule)"></div>
  <div class="abs" style="left:620px;top:2236px;width:450px;height:1px;background:var(--rule)"></div>

  <div class="avatar" role="img" aria-label="Portrait of worker in hard hat" style="left:144px;top:2086px"></div>
  <div class="quote" style="left:238px;top:2090px"><p>Nulla consequat massa quis enim. Donec pede justo, fringilla vel, aliquet nec, vulputate eget, arcu. In enim justo, rhoncus ut, imperdiet a, venenatis vitae, justo. Nullam dictum felis eu pede mollis pretium. Integer tincidunt. Cras dapibus.</p><div class="who">Martha L. Crane</div><div class="role">Marketing - <span>RoamGuide</span></div></div>

  <div class="avatar" role="img" aria-label="Portrait of worker in hard hat" style="left:622px;top:2086px"></div>
  <div class="quote" style="left:716px;top:2090px"><p>In enim justo, rhoncus ut, imperdiet a, venenatis vitae, justo. Nullam dictum felis eu pede mollis pretium. Integer tincidunt. Cras dapibus.</p><div class="who">Anna Velloso</div><div class="role">CEO - <span>InfoDepot</span></div></div>

  <div class="avatar" role="img" aria-label="Portrait of worker in hard hat" style="left:144px;top:2256px"></div>
  <div class="quote" style="left:238px;top:2260px"><p>Nulla consequat massa quis enim. Donec pede justo, fringilla vel, aliquet nec, vulputate eget, arcu.</p><div class="who">Maxi Morrow</div><div class="role">Public Relations - <span>Max Signalnet</span></div></div>

  <div class="avatar" role="img" aria-label="Portrait of worker in hard hat" style="left:622px;top:2256px"></div>
  <div class="quote" style="left:716px;top:2260px"><p>In enim justo, rhoncus ut, imperdiet a, venenatis vitae, justo. Nullam dictum felis eu pede mollis pretium. Integer tincidunt. Cras dapibus.</p><div class="who">Dr. Halvorsen</div><div class="role">Dean of Medicine - <span>Gloam Inc</span></div></div>
</section>

<section class="cta-band" role="img" aria-label="Blurred industrial workshop background">
  <div class="cta-box">
    <p>Start your no-strings-attached free trial! Your first 30 Days of use are free and if you are unsatisfied at any point in the future we give you a full refund on your last payment!</p>
    <a class="cta-btn">Apply Now</a>
  </div>
</section>

<footer class="site-footer">
  <div class="f-col" style="left:144px;width:200px">
    <h5>INTERESTING LINKS</h5>
    <p>Bellow are some interesting links for you! Enjoy your stay :)</p>
    <div class="social">
      <div><i style="background:#3aa3e3"></i>6664<br>Followers</div>
      <div><i style="background:#f08a24"></i>Subscribe<br>to News Feed</div>
    </div>
  </div>
  <div class="f-col" style="left:398px;width:200px">
    <h5>LATEST NEWS</h5>
    <div class="news"><i></i><span>Default Post with Preview Image - beautiful<small>December 12, 2012 - 9:11 pm</small></span></div>
    <div class="news"><i></i><span>This is a standard post format with preview Picture<small>January 14, 2012 - 1:13 pm</small></span></div>
    <div class="news"><i></i><span>Postformat Gallery: Multiple images with different sizes<small>January 14, 2012 - 1:13 pm</small></span></div>
  </div>
  <div class="f-col" style="left:646px;width:220px">
    <h5>TAGS</h5>
    <div class="tags"><span>are</span><span>nice</span><span>some</span><span>tags</span><span>these</span></div>
    <h5 style="margin-top:34px">CATEGORIES</h5>
    <div class="cats">Job Training Programs<br>Training Support and Features<br>Seminars and Workshops<br>Browse Training Library</div>
  </div>
  <div class="f-col" style="left:898px;width:200px">
    <h5>BUSINESS HOURS</h5>
    <p>Our support Hotline is available 24 Hours a day: (555) 010 234 5678</p>
    <p style="margin-top:16px"><b style="color:#fff">Monday-Friday:</b> 9am to 5pm<br><b style="color:#fff">Saturday:</b> 10am to 2pm<br><b style="color:#fff">Sunday:</b> Closed</p>
  </div>
</footer>

<div class="bottom-bar">
  <div class="copy">© Copyright - <span>SKILLSPAN</span></div>
  <nav class="bottom-nav"><a class="on">Home</a>|<a>Course</a>|<a>Faculty</a>|<a>Fees and Funding</a>|<a>testimonials</a>|<a>Faq</a>|<a>Contact Us</a></nav>
</div>

</body>
</html>
```